Meadowbrook Foundation Brochure

We are looking for a new brochure design for our foundation. The foundation is a nonprofit organization that provides assistance to special needs families in Indiana. We do this by providing ipads, communication software, gas cards, and financial assistance to families for their special needs child.

Target Market(s)

Families

Industry/Entity Type

Foundation

Colors
0355a3
3176b5
34a6d7
9bcb3b

Requirements
Must have
• Clear concise information

```html
<!DOCTYPE html>
<html lang="en">
<head>
<meta charset="utf-8">
<title>Meadowbrook Foundation Brochure</title>
<link href="https://fonts.googleapis.com/css2?family=Open+Sans:ital,wght@0,400;0,600;0,700;0,800;1,400;1,700&display=swap" rel="stylesheet">
<style>
  :root {
    --navy: #0355a3;
    --blue: #3176b5;
    --sky: #34a6d7;
    --green: #9bcb3b;
    --ink: #3a3a3a;
    --paper: #ffffff;
    --stage-top: #5ccbef;
    --stage-bottom: #2f7f98;
  }
  * { box-sizing: border-box; margin: 0; padding: 0; }
  html, body { width: 1200px; height: 951px; overflow: hidden; }
  body {
    font-family: "Open Sans", Arial, sans-serif;
    background: linear-gradient(160deg, var(--stage-top), var(--stage-bottom));
    position: relative;
    color: var(--ink);
  }
  .brochure {
    position: absolute;
    left: 100px; top: 155px;
    width: 1000px; height: 640px;
    background: var(--paper);
    overflow: hidden;
    box-shadow: 0 18px 40px rgba(0,0,0,.25);
  }
  .fold {
    position: absolute; left: 500px; top: 0; width: 1px; height: 640px;
    background: rgba(0,0,0,.08);
  }
  .shapes { position: absolute; inset: 0; }
  .photo-swing {
    position: absolute; left: 0; top: 0; width: 240px; height: 320px;
    background: linear-gradient(180deg, #3e4a2c 0%, #6b7a45 35%, #b8c2a6 70%, #ffffff 100%);
  }
  .label {
    display: inline-block;
    background: var(--green);
    color: #fff;
    font-weight: 700;
    font-size: 15px;
    letter-spacing: .3px;
    text-transform: uppercase;
    padding: 3px 16px 3px 10px;
    border-radius: 0 8px 0 8px;
    margin-bottom: 8px;
  }
  .making-difference {
    position: absolute; left: 256px; top: 40px; width: 220px; color: #fff;
  }
  .making-difference .intro { font-style: italic; font-size: 11px; line-height: 1.35; opacity: .85; margin-bottom: 8px; }
  .help-list { list-style: none; font-style: italic; font-weight: 700; font-size: 12.5px; line-height: 1.5; }
  .help-list li::before { content: "\2713"; margin-right: 6px; font-style: normal; }
  .how-to-help { position: absolute; left: 30px; top: 336px; width: 440px; }
  .how-to-help p { font-size: 12.5px; line-height: 1.4; color: #333; }
  .grant-heading {
    margin: 16px 0 12px;
    color: var(--navy);
    font-weight: 800;
    font-size: 19px;
    line-height: 1.2;
    text-transform: uppercase;
  }
  .grant-steps { font-size: 12.5px; line-height: 1.45; padding-left: 18px; color: #444; }
  .grant-steps strong { color: #222; }
  .what-we-do { position: absolute; left: 790px; top: 40px; width: 190px; }
  .what-we-do p { font-size: 11.5px; line-height: 1.45; color: #444; text-align: justify; }
</style>
</head>
<body>
  <main class="brochure">
    <div class="photo-swing" role="img" aria-label="Photo of a smiling boy on a playground swing"></div>

    <svg class="shapes" width="1000" height="640" viewBox="0 0 1000 640" aria-hidden="true">
      <defs>
        <linearGradient id="motherChild" x1="0" y1="0" x2="1" y2="1">
          <stop offset="0" stop-color="#6f6a45"/>
          <stop offset=".5" stop-color="#2d2a2a"/>
          <stop offset="1" stop-color="#d94f8c"/>
        </linearGradient>
      </defs>
      <rect x="240" y="0" width="260" height="300" fill="var(--blue)"/>
      <path d="M480 285 Q750 300 1000 370 L1000 640 L500 640 L500 285 Z" fill="var(--blue)"/>
      <circle cx="628" cy="120" r="160" fill="var(--green)"/>
      <circle cx="620" cy="114" r="152" fill="url(#motherChild)" role="img" aria-label="Photo of a mother holding her young daughter outdoors"/>
    </svg>

    <div class="fold"></div>

    <section class="making-difference">
      <h2 class="label">Making a difference:</h2>
      <p class="intro">Below are just a few of the children we have assisted through the foundation. We assist families by:</p>
      <ul class="help-list">
        <li>Purchasing ipads</li>
        <li>Purchasing language software</li>
        <li>Providing gas cards</li>
        <li>Providing scholarships for therapy</li>
      </ul>
    </section>

    <section class="how-to-help">
      <h2 class="label">How can you help?</h2>
      <p>Consider making a donation to the Meadowbrook Families First Foundation. 100% of proceeds go directly to special needs families in Northern Indiana. You can write a check or visit www.mbfff.org/donate to make a donation online.</p>
      <h3 class="grant-heading">Do you have a special needs child? You may qualify for a grant. To find out:</h3>
      <ol class="grant-steps">
        <li>Visit <strong>www.mbfff.org</strong> and complete a grant inquiry form</li>
        <li>Complete the entire grant application</li>
        <li>Your application will be reviewed by the foundation and you will be contacted with more information.</li>
      </ol>
    </section>

    <section class="what-we-do">
      <h2 class="label">What we do:</h2>
      <p>The Meadowbrook Families First Foundation provides assistance to special needs families in whatever way they may need it. For some families that is easing the financial burden of therapy, for others it is providing an ipad and language software so their nonverbal child can communicate. For others, it may mean providing diapers or clothing or gas cards to drive their children to doctor's appointments. We understand that each family is unique and that means assisting them in different ways, and we are here to do that.</p>
    </section>
  </main>
</body>
</html>
```